Willow Brook Meadows - Pelham Ridge Loop

Please use this range of Flyers. Info can be found on our Facebook Page Willow Brook Meadows. W

Colour range- Black with Orange Trim. Logo attached.

Target Market(s)

Horse Owners

Colors
ffcf3e
f78f20
f37122

Requirements
Must have
• Our Logo. Tri-fold
Should not have
• Other photos other than supplied. Do not mix Willow Brook Meadows with Willow Brook Equine Sanctuary. This is only for Willow Brook Meadows.

```html
<!DOCTYPE html>
<html lang="en">
<head>
<meta charset="utf-8">
<title>Willow Brook Meadows – Tri-fold Brochure</title>
<link href="https://fonts.googleapis.com/css2?family=Cinzel:wght@600;700&family=Oswald:wght@500;600&family=Open+Sans:wght@400;600&display=swap" rel="stylesheet">
<style>
  :root{
    --bg:#d7d8d9;
    --brown-dark:#1f130b;
    --brown:#3a2414;
    --brown-mid:#4d301b;
    --orange:#f37122;
    --orange-mid:#f78f20;
    --gold:#ffcf3e;
    --cream:#f4ece2;
    --white:#ffffff;
    --text-soft:#d9c9b8;
  }
  *{box-sizing:border-box;margin:0;padding:0}
  html,body{width:1200px;height:2400px;overflow:hidden}
  body{background:var(--bg);font-family:"Open Sans",Arial,sans-serif;position:relative}

  .spread{position:absolute;left:30px;width:1140px;height:880px;display:flex;box-shadow:0 10px 30px rgba(0,0,0,.25)}
  .spread--outside{top:220px}
  .spread--inside{top:1300px}
  .panel{position:relative;width:380px;height:100%;overflow:hidden;background:linear-gradient(180deg,var(--brown) 0%,var(--brown-dark) 100%)}
  .panel + .panel{border-left:1px solid rgba(0,0,0,.25)}

  .photo{position:absolute;left:0;width:100%}
  .photo--arena{background:linear-gradient(160deg,#7a8a5c 0%,#8d6a45 45%,#3b2a1c 100%)}
  .photo--rider{background:linear-gradient(170deg,#9aa57a 0%,#7b5836 50%,#2e1f14 100%)}
  .photo--trailer{background:linear-gradient(150deg,#a9b4ad 0%,#7a3d2a 55%,#3a2418 100%)}
  .photo--pasture{background:linear-gradient(160deg,#a7b07d 0%,#6d7a4b 50%,#4a3524 100%)}
  .photo--stable{background:linear-gradient(160deg,#8a9a6a 0%,#6a4a30 55%,#2f2016 100%)}

  .body-copy{color:var(--text-soft);font-size:13.5px;line-height:1.6}
  .headline{font-family:"Oswald",Arial,sans-serif;font-weight:600;font-size:28px;letter-spacing:1px;color:var(--white);text-transform:uppercase}
  .headline span{color:var(--orange)}

  /* outside: intro panel */
  .intro{position:absolute;left:32px;right:32px;top:380px}
  .intro .body-copy + .body-copy{margin-top:18px}
  .intro .headline{margin-bottom:16px;font-size:24px}

  /* outside: contact panel */
  .contact{position:absolute;left:36px;right:30px;top:390px}
  .contact-row{display:flex;align-items:center;gap:14px;margin-bottom:18px;color:var(--white);font-size:13.5px}
  .icon{width:38px;height:38px;background:var(--orange);display:flex;align-items:center;justify-content:center;flex-shrink:0}
  .brand{display:flex;align-items:center;gap:12px;font-family:"Oswald",Arial,sans-serif;font-weight:600;color:var(--orange);text-transform:uppercase;letter-spacing:1px;line-height:1.15}
  .brand-mark{width:34px;height:34px;background:var(--orange);flex-shrink:0}
  .contact .brand{margin-top:46px;font-size:20px}

  /* outside: cover panel */
  .cover-top{position:absolute;top:0;left:0;width:100%;height:190px;background:var(--white);display:flex;align-items:center;justify-content:flex-end;padding-right:34px}
  .cover-top .brand{font-size:26px;text-align:right}
  .cover-top .brand-mark{width:46px;height:46px}
  .cover-title{position:absolute;left:0;right:0;top:620px;text-align:center}
  .tagline{font-family:"Oswald",Arial,sans-serif;font-weight:500;color:var(--white);letter-spacing:5px;font-size:17px}
  .title{font-family:"Cinzel",Georgia,serif;font-weight:700;color:var(--orange);font-size:46px;line-height:1.05;margin-top:8px}
  .title--second{font-size:36px;color:var(--orange-mid)}
  .phone-bar{display:inline-flex;align-items:center;gap:10px;margin-top:18px;background:var(--orange);color:var(--white);font-weight:600;font-size:17px;padding:8px 22px;border-radius:20px}

  /* inside */
  .panel--orange{background:linear-gradient(180deg,var(--orange-mid) 0%,var(--orange) 100%)}
  .panel--orange .body-copy{color:var(--brown-dark)}
  .panel--orange .headline{color:var(--white)}
  .panel--orange .headline span{color:var(--brown-dark)}
  .block{position:absolute;left:30px;right:30px}
  .block .headline{margin-bottom:12px}
  .rule{width:60px;height:4px;background:var(--orange);margin-bottom:14px}
  .panel--orange .rule{background:var(--brown-dark)}
</style>
</head>
<body>

<!-- Outside spread -->
<section class="spread spread--outside" aria-label="Brochure outside">
  <div class="panel panel--intro">
    <div class="photo photo--arena" style="top:0;height:340px" role="img" aria-label="Photo of a rider jumping a horse in an arena"></div>
    <div class="intro">
      <h2 class="headline">About <span>Us</span></h2>
      <p class="body-copy">Set on open pasture, our grounds welcome riders of every level. Lessons, boarding and trail rides run all year, with calm horses and patient staff ready to help you grow in the saddle.</p>
      <p class="body-copy">Explore the Pelham Ridge Loop, a shaded trail that winds past creeks and meadows. Guided outings leave each morning.</p>
    </div>
  </div>

  <div class="panel panel--contact">
    <div class="photo photo--arena" style="top:0;height:340px;background-position:right" role="img" aria-label="Photo continuing the arena jumping scene"></div>
    <div class="contact">
      <div class="contact-row">
        <span class="icon"><svg width="20" height="20" viewBox="0 0 24 24"><path fill="#fff" d="M6.6 10.8a15 15 0 0 0 6.6 6.6l2.2-2.2a1 1 0 0 1 1-.25 11.4 11.4 0 0 0 3.6.57 1 1 0 0 1 1 1V20a1 1 0 0 1-1 1A17 17 0 0 1 3 4a1 1 0 0 1 1-1h3.5a1 1 0 0 1 1 1c0 1.25.2 2.45.57 3.6a1 1 0 0 1-.25 1z"/></svg></span>
        <span>(555) 014-2286</span>
      </div>
      <div class="contact-row">
        <span class="icon"><svg width="20" height="20" viewBox="0 0 24 24"><rect x="3" y="6" width="18" height="12" fill="none" stroke="#fff" stroke-width="2"/><path d="M3 6l9 7 9-7" fill="none" stroke="#fff" stroke-width="2"/></svg></span>
        <span>hello@willowbrookmeadows.example</span>
      </div>
      <div class="contact-row">
        <span class="icon"><svg width="20" height="20" viewBox="0 0 24 24"><circle cx="12" cy="12" r="9" fill="none" stroke="#fff" stroke-width="2"/><path d="M3 12h18M12 3c3 3 3 15 0 18M12 3c-3 3-3 15 0 18" fill="none" stroke="#fff" stroke-width="1.6"/></svg></span>
        <span>www.willowbrookmeadows.example</span>
      </div>
      <div class="contact-row">
        <span class="icon"><svg width="20" height="20" viewBox="0 0 24 24"><path fill="#fff" d="M12 2a7 7 0 0 0-7 7c0 5 7 13 7 13s7-8 7-13a7 7 0 0 0-7-7zm0 9.5A2.5 2.5 0 1 1 12 6.5a2.5 2.5 0 0 1 0 5z"/></svg></span>
        <span>48 Meadow Lane, Pelham Ridge</span>
      </div>
      <div class="brand"><span class="brand-mark"></span><span>Willow Brook<br>Meadows</span></div>
    </div>
  </div>

  <div class="panel panel--cover">
    <div class="cover-top">
      <div class="brand"><span>Willow Brook<br>Meadows</span><span class="brand-mark"></span></div>
    </div>
    <div class="photo photo--rider" style="top:190px;height:410px" role="img" aria-label="Photo of a rider on a horse in the arena"></div>
    <div class="cover-title">
      <p class="tagline">MULTI-FACETED</p>
      <p class="title">EQUINE</p>
      <p class="title title--second">DESTINATION</p>
      <span class="phone-bar"><svg width="16" height="16" viewBox="0 0 24 24"><path fill="#fff" d="M6.6 10.8a15 15 0 0 0 6.6 6.6l2.2-2.2a1 1 0 0 1 1-.25 11.4 11.4 0 0 0 3.6.57 1 1 0 0 1 1 1V20a1 1 0 0 1-1 1A17 17 0 0 1 3 4a1 1 0 0 1 1-1h3.5a1 1 0 0 1 1 1c0 1.25.2 2.45.57 3.6a1 1 0 0 1-.25 1z"/></svg>(555) 014-2286</span>
    </div>
  </div>
</section>

<!-- Inside spread -->
<section class="spread spread--inside" aria-label="Brochure inside">
  <div class="panel">
    <div class="photo photo--trailer" style="top:0;height:250px" role="img" aria-label="Photo of a horse beside a red trailer"></div>
    <div class="block" style="top:280px">
      <h2 class="headline">Your <span>Headline</span></h2>
      <div class="rule"></div>
      <p class="body-copy">Our arena and stables are kept clean and safe. Book a visit to meet the herd, tour the barns and plan your next ride with us.</p>
    </div>
    <div class="photo photo--pasture" style="top:600px;height:280px" role="img" aria-label="Photo of a saddled horse in the paddock"></div>
  </div>

  <div class="panel panel--orange">
    <div class="block" style="top:50px">
      <h2 class="headline">Your <span>Headline</span></h2>
      <div class="rule"></div>
      <p class="body-copy">Our arena and stables are kept clean and safe. Book a visit to meet the herd, tour the barns and plan your next ride with us.</p>
    </div>
    <div class="block" style="top:360px;right:150px">
      <h2 class="headline">Your <span>Headline</span></h2>
      <div class="rule"></div>
      <p class="body-copy">Our arena and stables are kept clean and safe. Book a visit to meet the herd, tour the barns and plan your next ride with us.</p>
    </div>
    <div class="photo photo--arena" style="top:640px;left:160px;width:220px;height:240px" role="img" aria-label="Photo of a rider schooling a horse"></div>
  </div>

  <div class="panel">
    <div class="photo photo--stable" style="top:0;height:250px" role="img" aria-label="Photo of the barn and grounds"></div>
    <div class="block" style="top:280px">
      <h2 class="headline">Your <span>Headline</span></h2>
      <div class="rule"></div>
      <p class="body-copy">Our arena and stables are kept clean and safe. Book a visit to meet the herd, tour the barns and plan your next ride with us.</p>
    </div>
    <div class="photo photo--rider" style="top:600px;height:280px" role="img" aria-label="Photo of a rider leading a horse"></div>
  </div>
</section>

</body>
</html>
```